Presentation Design - Gable Works Sales Presentation

I am partnering up with Gable Works, I need to help build their brand and first we are going to start with a sales and estimate presentation / binder that includes individual pdfs / flyers . I am going to give you copies of their current stuff along with the pdfs / flyers that you created for Tidewell Siding and I am looking for a design that is consistent throughout. Elegant, professional, and on brand to Gable Works. Here is a list of things I am looking to start with that will be included into the sales presentation binder. ALSO, Gable Works does not currently have a company slogan. We need to come up with ideas for that. Gable Works will be a lot different play than Tidewell Siding as with Tidewell there was a lot of humor / puns / etc. involved to help play off the name and recoginition. Gable Works is a bit different. They have the reputation and longevity that speaks VOLUME and QUALITY along with their relationships so it needs to be more of a professional yet grabs your attention and makes you want to know more or fits the brand.
Ok heres the list of things im thinking of beginning with. Please also let me know what else you think I can add after seeing my vision with this.
- Meet the Team (Office / Supplementing / Production / Estimating / Owner / Marketing / Etc - the people the customers dont usually meet) - Behind the Scenes page (displaying the full service metal shop and the team / the brick & mortar office / the trucks & equipment)
-Services Offered Page
- Why Gable Works. (2 - 3 page pdf : detailed / comparison chart (like one that has gable works vs. other contractor diagram things with check marks and red x's for the "other contractors" to show a good visual of how we are different)
-Credentials Page (different certifications we have and brands we are partnered with)
-Gable Works. Warranty
-References Page (one for residential and one for commercial)
-Reviews Page (showing 3-5 reviews left by customers with a qr code that links directly to the reviews on google page if theyd like to see more)
- A getting to know the rep page (each rep will need to individually get this created - I will upload the one i already have for me you created previously)
-FAQ's page regarding roofing, siding & storm damage restoration projects
-Pre Construction / Build Checklist : What to expect (for each trade: roofing, siding, gutters, windows & doors)
-A page displaying previous work/jobs completed (this would showcase higher end projects)

Gable Workshop (Gable Works.) Details:
- Been in business since 1992
-Family owned (not PE like a lot of companies now a days)
-10,000 plus projects completed
- Serving all of MN
-Real Roofers not paper contractors
-In house commercial division / repair & maintenance division / specializing in residential, commercial, & multi family

Certifications
-PLM / Brandt Halvik / Surevault / UVR / & Penhollow
-TCQ a+ rated
-4.9 Star Rating on google with over 100 reviews
-Listwelle
-Federated Eave Builders Guild Creditation (FEBG)
-Pinewood Slat & Tile Council
-Morvella
-QT Trimflex
-Zenth Tile
Plus any other useful certifications you may think would be useful to add onto their like the other tidewell siding page you created.

-in house full service metal shop
-Dedicated production managers
-In house supplementer / estimator
-Brick & mortar
-Full time & in house crews (been with gable works over 20 years) most companies all use subs and dont know who the crews actually even are
-In house repair & maintenance division
-Avg. Install 2 weeks vs. months
-Project Supervision & quality control
-Yard guard protection systems (yard guard is a brand can use their logo)
-In house dumpsters & rolloffs

Please use photos from the website. The website is gableworksmn.example

I am going to attach the other designs you created for me previously that I like and want those just recreated along with other types of flyers I am wanting created as ideas for you and copy of Gable Works's current flyer

Industry/Entity Type

Roofing / Exteriors / Storm Damage Restoration

Font styles to use
Other font styles liked:
• Helvetica font we can try it with to start.

Colors
EB3D1F
EC4F4E
F09395
F8D3D4
FCEDEE

Requirements
Must have
• The multiple pages as requested. Go to Gable Workshop NA. Inc , facebook page to get photos to add to flyers

```html
<!DOCTYPE html>
<html lang="en">
<head>
<meta charset="utf-8">
<title>Gable Works – FAQ's</title>
<link rel="stylesheet" href="https://fonts.googleapis.com/css2?family=Poppins:wght@400;600;700;800&display=swap">
<style>
  :root {
    --ink: #1c1c1e;
    --red: #eb3d1f;
    --red-soft: #ec4f4e;
    --paper: #ffffff;
    --backdrop: #ececec;
    --rule: #9a9a9a;
    --body: #2a2a2a;
  }
  * { box-sizing: border-box; margin: 0; padding: 0; }
  html, body { width: 1200px; height: 1200px; overflow: hidden; }
  body {
    background: var(--backdrop);
    font-family: "Poppins", Helvetica, Arial, sans-serif;
    color: var(--body);
  }
  .flyer {
    position: absolute;
    left: 150px; top: 18px;
    width: 900px; height: 1164px;
    background: var(--paper);
    overflow: hidden;
    box-shadow: 0 6px 24px rgba(0,0,0,0.12);
  }
  .flyer-shapes { position: absolute; inset: 0; }
  .slogan {
    position: absolute; left: 500px; top: 44px;
    color: #fff; font-weight: 800; font-size: 27px; line-height: 1.2;
  }
  .brand {
    position: absolute; left: 70px; top: 62px;
    display: flex; align-items: center; gap: 12px;
  }
  .brand-dot { width: 34px; height: 34px; border-radius: 50%; background: var(--red); }
  .brand-name { font-weight: 800; font-size: 34px; color: var(--ink); letter-spacing: 0.5px; }
  .faq-title {
    position: absolute; left: 390px; top: 160px;
    font-weight: 800; font-size: 34px; color: var(--ink);
  }
  .faq-list {
    position: absolute; left: 80px; top: 214px; width: 756px;
    list-style: none;
  }
  .faq-item { padding: 8px 0 9px; border-bottom: 1px solid var(--rule); }
  .faq-item:last-child { border-bottom: none; }
  .faq-q { font-weight: 700; font-size: 16.5px; color: var(--ink); line-height: 1.3; }
  .faq-a { font-size: 12px; line-height: 1.42; margin-top: 3px; }
  .footer {
    position: absolute; left: 0; bottom: 44px; width: 900px; height: 58px;
    display: flex; align-items: center; justify-content: space-between;
    padding: 0 34px 0 50px;
    color: #fff; font-size: 10px; font-weight: 600; white-space: nowrap;
  }
  .contact { display: flex; align-items: center; gap: 7px; white-space: nowrap; }
  .contact svg { width: 18px; height: 18px; flex: none; }
  .license {
    position: absolute; right: 22px; bottom: 112px;
    color: #fff; font-size: 11px; font-weight: 700;
  }
</style>
</head>
<body>
  <article class="flyer">
    <svg class="flyer-shapes" viewBox="0 0 900 1164" aria-hidden="true">
      <polygon points="440,0 900,0 900,150 420,168" fill="var(--ink)"/>
      <polygon points="370,26 430,0 418,96 384,124" fill="var(--red)"/>
      <polygon points="900,150 900,380 862,420 862,230" fill="var(--red)"/>
      <polygon points="900,380 900,520 880,540 880,400" fill="var(--ink)"/>
      <polygon points="0,430 52,400 52,650 0,690" fill="var(--ink)"/>
      <polygon points="0,700 52,664 52,900 0,950" fill="var(--red)"/>
      <rect x="0" y="1062" width="900" height="58" fill="var(--ink)"/>
      <rect x="0" y="1120" width="900" height="44" fill="var(--red)"/>
      <polygon points="720,1018 900,1000 900,1062 700,1062" fill="var(--red-soft)"/>
    </svg>

    <div class="slogan">Built on Trust.<br>Backed by Strength.</div>

    <div class="brand">
      <span class="brand-dot"></span>
      <span class="brand-name">Gable Works</span>
    </div>

    <h1 class="faq-title">FAQ'S</h1>

    <ul class="faq-list">
      <li class="faq-item">
        <p class="faq-q">What are the primary components of a roof system?</p>
        <p class="faq-a">A standard residential roofing system consists of five main components: Roof Decking (sheathing), Underlayment, Roof Flashings, Ventilation Products, and Shingles. Together, these layers create a sealed barrier to protect your home.</p>
      </li>
      <li class="faq-item">
        <p class="faq-q">What happens if rotten wood is discovered during a tear-off?</p>
        <p class="faq-a">Roof rot or fungal decay isn't always visible during the initial inspection. If we discover damaged wood once the old shingles are removed, it must be replaced with new wood to ensure structural integrity. These additional charges are applied at fair market value.</p>
      </li>
      <li class="faq-item">
        <p class="faq-q">Is a roofing permit required for my project?</p>
        <p class="faq-a">In most municipalities, a building permit is required for any roof work meeting minimum square footage requirements. When you hire Gable Workshop NA. Inc, we handle the logistics and will apply for all necessary building permits on your behalf.</p>
      </li>
      <li class="faq-item">
        <p class="faq-q">How do I know if I need a full replacement or just a repair?</p>
        <p class="faq-a">While some damage is purely cosmetic and only requires a minor repair, significant aging or storm damage may warrant a full replacement. The most accurate way to determine the health of your roof is to schedule a professional inspection with our team.</p>
      </li>
      <li class="faq-item">
        <p class="faq-q">Can you help with storm damage repairs?</p>
        <p class="faq-a">Absolutely. We have extensive experience in restoring homes after hail, wind, and storm events. We can assess the damage and help restore your home to its pre-storm condition efficiently.</p>
      </li>
      <li class="faq-item">
        <p class="faq-q">Why am I required to pay my insurance deductible?</p>
        <p class="faq-a">It's the law. Under Minnesota Statute § 325E.66, contractors are prohibited from offering to pay a customer's insurance deductible or providing any compensation as an inducement to enter a contract. Violating this state law can result in fines of up to $10,000 per violation.</p>
      </li>
      <li class="faq-item">
        <p class="faq-q">Why do estimates vary so much between companies?</p>
        <p class="faq-a">A lower estimate often reflects "cut-rate" installation practices or inferior products, which can lead to higher costs down the road. We prioritize transparency and high-quality materials to ensure you receive a long-term investment that protects your home.</p>
      </li>
      <li class="faq-item">
        <p class="faq-q">Should I be home during the installation?</p>
        <p class="faq-a">It is not necessary for you to be home during the process unless you have skylights that need internal attention. We just ask that you provide clear access to the driveway and backyard for our crews.</p>
      </li>
      <li class="faq-item">
        <p class="faq-q">How long does a typical installation take?</p>
        <p class="faq-a">Most installations are completed within one to four working days. Please note that weather conditions and the complexity/detail of your specific roof can impact the final timeline.</p>
      </li>
      <li class="faq-item">
        <p class="faq-q">What other exterior services do you offer?</p>
        <p class="faq-a">Beyond roofing, we provide expert installation and repair for Gutters, Siding, Insulation, and Window Replacement.</p>
      </li>
    </ul>

    <div class="license">MN LIC #BC480917</div>

    <footer class="footer">
      <span class="contact">
        <svg viewBox="0 0 20 20"><circle cx="10" cy="10" r="9" fill="none" stroke="#fff" stroke-width="1.5"/><path d="M10 4.5a3.5 3.5 0 0 0-3.5 3.5c0 2.6 3.5 6.5 3.5 6.5s3.5-3.9 3.5-6.5A3.5 3.5 0 0 0 10 4.5z" fill="#fff"/><circle cx="10" cy="8" r="1.2" fill="var(--ink)"/></svg>
        1420 Larkspur Ave NE, Elm Hollow, MN 55012
      </span>
      <span class="contact">
        <svg viewBox="0 0 20 20"><circle cx="10" cy="10" r="9" fill="none" stroke="#fff" stroke-width="1.5"/><rect x="5" y="6.5" width="10" height="7" rx="1" fill="#fff"/><path d="M5.5 7l4.5 3.5L14.5 7" fill="none" stroke="var(--ink)" stroke-width="1"/></svg>
        info@gableworksmn.example
      </span>
      <span class="contact">
        <svg viewBox="0 0 20 20"><circle cx="10" cy="10" r="9" fill="none" stroke="#fff" stroke-width="1.5"/><path d="M7 5.5l2 2-1.2 1.3a6 6 0 0 0 3.4 3.4l1.3-1.2 2 2-1.3 1.5C9.5 14.5 5.5 10.5 5.5 6.8z" fill="#fff"/></svg>
        (763)-555-0182
      </span>
      <span class="contact">
        <svg viewBox="0 0 20 20"><circle cx="10" cy="10" r="9" fill="none" stroke="#fff" stroke-width="1.5"/><circle cx="10" cy="10" r="5" fill="none" stroke="#fff" stroke-width="1.2"/><path d="M5 10h10M10 5c-2 3-2 7 0 10M10 5c2 3 2 7 0 10" fill="none" stroke="#fff" stroke-width="1"/></svg>
        www.gableworksmn.example
      </span>
    </footer>
  </article>
</body>
</html>
```